Business Card Design

we are a brand new cable TV network devoted to self improvement and leading a better life called FLOURIVO TV.I have a logo. We have 3 executives that need cards.I want it to be a heavy stock card: professional but showing our creative nature

Industry/Entity Type

Business

Contact Information for Business Card

CLAUDIA SAENZ AMLIECEO350 San Juan DrPonte Vedra Beach FL 32082904-473-5953

```html
<!DOCTYPE html>
<html lang="en">
<head>
<meta charset="utf-8">
<title>FLOURIVO TV – Business Card</title>
<link href="https://fonts.googleapis.com/css2?family=Lato:wght@400;700&display=swap" rel="stylesheet">
<style>
  :root {
    --page-bg: #e6e6e6;
    --card-bg: #f8f8f8;
    --ink: #231f20;
    --brand-red: #d42028;
    --band-dark: #211612;
  }
  html, body {
    margin: 0;
    padding: 0;
    width: 1200px;
    height: 978px;
    overflow: hidden;
    background: var(--page-bg);
    font-family: "Lato", sans-serif;
  }
  .card {
    position: absolute;
    left: 50px;
    top: 175px;
    width: 1100px;
    height: 628px;
    background: var(--card-bg);
    color: var(--ink);
  }
  .brand-name {
    position: absolute;
    left: 51px;
    top: 78px;
    margin: 0;
    font-size: 96px;
    font-weight: 700;
    line-height: 1;
    letter-spacing: -1px;
    color: var(--ink);
  }
  .person {
    position: absolute;
    right: 61px;
    top: 288px;
    text-align: right;
  }
  .person-name {
    margin: 0;
    font-size: 32px;
    font-weight: 700;
    line-height: 40px;
  }
  .person-title {
    margin: 4px 0 0;
    font-size: 36px;
    font-weight: 400;
    line-height: 42px;
    color: var(--brand-red);
    letter-spacing: 1px;
  }
  .divider {
    position: absolute;
    left: 51px;
    right: 61px;
    top: 388px;
    height: 3px;
    background: var(--ink);
  }
  .contact {
    position: absolute;
    left: 51px;
    top: 456px;
    font-size: 28px;
    line-height: 37px;
  }
  .contact-row {
    display: flex;
    align-items: center;
  }
  .contact-icon {
    width: 30px;
    height: 30px;
    margin-right: 11px;
    flex: none;
  }
  .contact-row.indent {
    padding-left: 41px;
  }
  .bottom-band {
    position: absolute;
    left: 0;
    top: 0;
    width: 100%;
    height: 100%;
    pointer-events: none;
  }
</style>
</head>
<body>
  <section class="card">
    <h1 class="brand-name">FLOURIVO TV</h1>

    <div class="person">
      <p class="person-name">MIRELLA OKAFOR DUNST</p>
      <p class="person-title">CEO</p>
    </div>

    <div class="divider"></div>

    <div class="contact">
      <div class="contact-row">
        <svg class="contact-icon" viewBox="0 0 24 24" aria-hidden="true">
          <path fill="#d42028" d="M2 9c0-3 4-5 10-5s10 2 10 5v2h-5V9.5c-1.5-.6-3.2-.9-5-.9s-3.5.3-5 .9V11H2z"/>
          <path fill="#d42028" d="M6 12l2-3h8l2 3v7H6z"/>
          <circle cx="12" cy="15" r="2.3" fill="#f8f8f8"/>
        </svg>
        <span>904-618-2047</span>
      </div>
      <div class="contact-row">
        <svg class="contact-icon" viewBox="0 0 24 24" aria-hidden="true">
          <path fill="#d42028" d="M12 1C7.6 1 4.5 4.3 4.5 8.5 4.5 14 12 23 12 23s7.5-9 7.5-14.5C19.5 4.3 16.4 1 12 1z"/>
          <circle cx="12" cy="8.5" r="3" fill="#f8f8f8"/>
        </svg>
        <span>718 Harlow Creek Dr</span>
      </div>
      <div class="contact-row indent">
        <span>Ponte Vedra Beach FL 32097</span>
      </div>
    </div>

    <svg class="bottom-band" viewBox="0 0 885 505" preserveAspectRatio="none" aria-hidden="true">
      <polygon fill="#211612" points="0,487 540,487 530,505 0,505"/>
      <polygon fill="#d42028" points="548,473 588,473 568,505 528,505"/>
      <polygon fill="#d42028" points="593,473 885,473 885,505 573,505"/>
    </svg>
  </section>
</body>
</html>
```